Australia-Wide Industry Leader Bookkeeping Business Website Design Required

We need a website designed for our 10 year old bookkeeping business, Barwick & Lund. Barwick & Lund has been servicing the local & interstate communities of Australia, providing first-class BAS & Bookkeeping services with a personal touch unmatched by anyone else in the county.

What began 10 years ago as a small business focusing on family, friends and the local community, it has since grown into a well respected business with 95% of their business based solely on word of mouth and personal referrals from around Australia.

We would like to see designs that incorporate our existing brand/logo. The colours to be used on the website should be colours that work well with our logo. The design should communicate maturity, trust and confidence with a Web 2.0 look and feel.

We have produced mockups of the entire website as well as assets used in the mockups. Please reference the attached files. The mockups are an example of all the design elements that we want on each page. Designers are encouraged to use the mockups as a guideline only and for designers to use their own creativity.
Updates

This message is for new graphic designers who are considering commencing work on this project. Thank you for expressing an interest in our project. We would like to inform you that this project is close to completion as we have a number designs under very serious consideration.

We are currently in a position where we are disinterested providing feedback to improve on new designs submitted. We will provide feedback to improve new designs only if the submitted designs are very close to what we want for our website, and will only require 1 or 2 revision rounds to refine before the project completion date we will not work with designers to refine their newly submitted designs.

We feel that it is important for all designers to know the above information as we feel that your time and effort may be better spent working on another project.

Thank you for your understanding.

A big thank you for all the designs submitted. We are now in the process of selecting a design. Please be patient during this process. Thank you.

Target Market(s)

Busy Business Owners

Industry/Entity Type

Small Business

Requirements
Must have
• We require a rectangular "slide show" type feature to serve as a "teaser" to arouse the emotions of our website visitors. Each slide asks a specific question. The questions are:

- Is your paperwork in a mess?
- Do you need to get organised for the end of financial year?
- Are you sick & tired of endless amounts of paperwork & BASs?
- Do you feel frustrated & annoyed because you know your books need to be done?
- Do you lack the time & patience to get your paperwork done?
- Do you wish you had more time to do the things you enjoy doing?
- Contact Barwick & Lund today and we will transform your chaos into order.

Underneath the slide show will be a button to "Call Barwick & Lund Now - 03 5550 1827".

```html
<!DOCTYPE html>
<html lang="en">
<head>
<meta charset="utf-8">
<title>Barwick &amp; Lund – Bookkeeping</title>
<link rel="stylesheet" href="https://fonts.googleapis.com/css2?family=Sorts+Mill+Goudy&family=Arimo:wght@400&display=swap">
<style>
:root{
  --red:#8a0a0a;
  --red-bright:#c11;
  --ink:#333;
  --grey:#666;
  --line:#d6d6d6;
  --panel:#f2f2f2;
  --tick:#7cb018;
  --dot:#9ac21f;
  --page:#fff;
  --outer:#f0f0f0;
}
*{margin:0;padding:0;box-sizing:border-box}
html,body{width:705px;height:1200px;overflow:hidden;background:var(--outer)}
body{font-family:"Arimo",Arial,sans-serif;color:var(--grey)}
.page{position:relative;width:590px;height:1200px;margin-left:58px;background:var(--page)}
.abs{position:absolute}
.serif{font-family:"Sorts Mill Goudy",Georgia,serif}

.brand{left:171px;top:15px;width:247px;height:48px;border:1px solid #222;display:flex;align-items:center;justify-content:center;gap:8px}
.brand-mark{width:14px;height:14px;background:var(--red)}
.brand-name{font-family:"Sorts Mill Goudy",Georgia,serif;font-size:28px;color:var(--red);line-height:1}

.nav{left:12px;top:77px;width:565px;height:23px;display:flex;border:1px solid var(--line);background:linear-gradient(#fafafa,#e9e9e9)}
.nav a{font-family:"Sorts Mill Goudy",Georgia,serif;font-size:10px;color:#555;text-decoration:none;display:flex;align-items:center;justify-content:center;border-right:1px solid var(--line)}
.nav a:last-child{border-right:none}
.nav a.current{background:linear-gradient(#d01a1a,#900);color:#fff}

.tagline{left:12px;top:109px;width:565px;font-size:15.5px;line-height:18px;color:var(--ink);text-align:center}

.slider{left:12px;top:172px;width:565px;height:210px;overflow:hidden}
.slide-art{width:100%;height:100%;background:linear-gradient(100deg,#6d6a4e 0%,#c9c39a 35%,#e5e0c4 55%,#2e5aa8 75%,#1f3f80 100%)}
.caption{left:0;bottom:0;width:100%;height:47px;background:rgba(40,40,40,.75);color:#fff;font-size:15px;line-height:16px;padding:6px 12px}
.dots{right:12px;bottom:10px;display:flex;gap:5px}
.dots i{width:8px;height:8px;border-radius:50%;background:#aaa;display:block}
.dots i.on{background:#fff}

h2{font-family:"Sorts Mill Goudy",Georgia,serif;font-weight:normal;color:var(--red);font-size:14px}
.intro{left:12px;top:433px;width:374px;font-size:7.3px;line-height:10.5px;text-align:justify}

.ticks{list-style:none;font-size:9.4px;color:#555}
.ticks li{display:flex;align-items:flex-start;gap:8px;height:17.6px}
.ticks svg{flex:none;width:13px;height:11px}
.sub{list-style:none;margin-left:10px}
.sub li{height:17.6px;display:flex;align-items:center;gap:8px}
.sub li::before{content:"";width:5px;height:5px;border-radius:50%;background:var(--dot)}
.note{left:12px;top:1024px;font-size:10px;color:var(--red)}

.call{left:428px;top:407px;width:149px;height:48px;border:1px solid var(--line);background:linear-gradient(#fafafa,#e6e6e6);display:flex;align-items:center;gap:10px;padding-left:10px}
.call-text{font-size:12px;color:#333;line-height:14px}
.call-text b{font-weight:normal;color:var(--red);font-size:13px}

.box{left:428px;width:149px;border:1px solid var(--line);background:var(--panel)}
.box-head{background:var(--red);color:#fff;font-family:"Sorts Mill Goudy",Georgia,serif;font-size:11.5px;padding:3px 5px;line-height:13px}
.reach{top:480px;height:230px}
.reach p{font-size:7px;line-height:8.6px;color:#333;padding:4px 5px}
.reach p span{color:var(--red)}
.map{left:0;top:73px;width:147px;height:156px;background:radial-gradient(ellipse at 50% 50%,#bdbdbd 0%,#c8c8c8 55%,#fff 56%)}
.quals{top:738px;height:189px}
.quals .box-head{text-align:center;height:35px;display:flex;align-items:center;justify-content:center}
.quals ul{list-style:none;padding:7px 5px;font-size:8px;color:#555}
.quals li{display:flex;gap:5px;margin-bottom:7px;line-height:9.5px}
.quals li svg{flex:none;width:10px;height:9px}

.badges{left:12px;top:1063px;width:565px;height:78px;display:flex;justify-content:space-between;align-items:center}
.badge{background:#ddd}
.footer-rule{left:12px;top:1165px;width:565px;border-top:1px dotted #999}
.follow{left:12px;top:1175px;font-size:8px;color:#333;display:flex;align-items:center;gap:6px}
.follow span.sq{width:13px;height:13px;background:#3b5998;display:block}
.follow span.sq.alt{background:#4ab3e6}
.copy{right:13px;top:1178px;font-size:8px;color:#333}
</style>
</head>
<body>
<svg width="0" height="0" style="position:absolute">
  <symbol id="tick" viewBox="0 0 13 11"><path d="M1 6 L5 10 L12 1" fill="none" stroke="#7cb018" stroke-width="2.6" stroke-linecap="round" stroke-linejoin="round"/></symbol>
  <symbol id="tick-red" viewBox="0 0 10 9"><path d="M1 5 L4 8 L9 1" fill="none" stroke="#8a0a0a" stroke-width="2.2" stroke-linecap="round" stroke-linejoin="round"/></symbol>
</svg>
<div class="page">
  <div class="abs brand"><span class="brand-mark"></span><span class="brand-name">Barwick &amp; Lund</span></div>

  <nav class="abs nav">
    <a class="current" style="width:62px">Home</a>
    <a style="width:70px">About us</a>
    <a style="width:64px">Services</a>
    <a style="width:84px">Testimonials</a>
    <a style="width:63px">Articles</a>
    <a style="width:90px">Endorsements</a>
    <a style="width:53px">Links</a>
    <a style="flex:1">Contact us</a>
  </nav>

  <p class="abs tagline serif">For nearly 10 years BARWICK &amp; LUND has been servicing the local &amp; interstate communities of Australia, providing first - class bas &amp; book keeping services with a personal touch un-matched by anyone else in the country .</p>

  <div class="abs slider">
    <div class="slide-art" role="img" aria-label="Photo of a stressed office worker beside a tall stack of blue folders"></div>
    <div class="abs caption">Do you feel frustrated &amp; annoyed because you know your books need to be done?</div>
    <div class="abs dots"><i></i><i></i><i></i><i class="on"></i><i></i><i></i><i></i></div>
  </div>

  <h2 class="abs" style="left:12px;top:397px">Welcome to Barwick &amp; Lund</h2>
  <p class="abs intro">Having worked for a certified accountant firm for numerous year, Helen Barwick &amp; Clare Lund become concerned about the consistency of inaccurate books prepared by other in various organization. As the quality of bookworm declined, the fees seemed to increased , together they identified a need for a quality bookkeeping that truly understood what being is business is all about &amp; more importantly how to correctly &amp; accurately process book according to the los &amp; requirement set by the Australian taxation office. They wanted to give people a batter alternative- thus Barwick &amp; Lund was born, what begin as a small business focusing on family, friend &amp; the local communities, has since grow in to a well respected business with 95% of their business based slowly on word of mouth &amp; personal referrals from around Australia.</p>

  <h2 class="abs" style="left:12px;top:536px">To summarise</h2>
  <ul class="abs ticks" style="left:12px;top:559px">
    <li><svg><use href="#tick"/></svg>Free initial consulting</li>
    <li><svg><use href="#tick"/></svg>Bookkeeping</li>
    <li><svg><use href="#tick"/></svg>Pay roll</li>
    <li><svg><use href="#tick"/></svg>Superannuation</li>
    <li><svg><use href="#tick"/></svg>Fuel tax credit</li>
    <li><svg><use href="#tick"/></svg>Ledgerline software &amp; training</li>
  </ul>
  <ul class="abs ticks" style="left:208px;top:559px">
    <li><svg><use href="#tick"/></svg>Register BAS agent #40512-118</li>
    <li><svg><use href="#tick"/></svg>BAS preparation &amp; lodgment</li>
    <li><svg><use href="#tick"/></svg>IAS preparation &amp; lodgment</li>
    <li><svg><use href="#tick"/></svg>Margined scheme</li>
    <li><svg><use href="#tick"/></svg>Offsite &amp; onsite bookkeeping</li>
    <li><svg><use href="#tick"/></svg>Australian wide</li>
  </ul>

  <h2 class="abs" style="left:12px;top:682px">What makes Barwick &amp; Lund different from other bookkeepers</h2>
  <ul class="abs ticks" style="left:12px;top:714px;width:360px">
    <li><svg><use href="#tick"/></svg>We guarantee we quality of our work</li>
    <li><svg><use href="#tick"/></svg>We have over 35 years of experienced</li>
    <li><svg><use href="#tick"/></svg>We have owned a operated business for 35 years</li>
    <li><svg><use href="#tick"/></svg>The Barwick &amp; Lund team are investors &amp; traders</li>
    <li><svg><use href="#tick"/></svg>Extensive business network for your benefits</li>
    <li><svg><use href="#tick"/></svg>Backed by a team of accountants</li>
    <li style="height:26px"><svg><use href="#tick"/></svg>We work with a team of elite accountants &amp; wealth Creation professionals who coach us monthly in the following:</li>
    <li style="height:auto;display:block"><ul class="sub">
      <li>Assets protection</li>
      <li>superannuation &amp; self managed superannuation funds</li>
      <li>property investing</li>
      <li>tax steatites, tax structure &amp; best tax saving</li>
    </ul></li>
    <li style="height:26px"><svg><use href="#tick"/></svg>We understand just how important it is to help lead &amp; guide our clients from making profits to:</li>
    <li style="height:auto;display:block"><ul class="sub">
      <li>maximum profits</li>
      <li>wealth creation</li>
      <li>tax minim station</li>
      <li>asset protection</li>
    </ul></li>
  </ul>
  <p class="abs note">This is something that other bookkeeper just don't do !</p>

  <div class="abs call">
    <svg width="28" height="24" viewBox="0 0 28 24"><path d="M2 8 Q14 -2 26 8 L22 11 L19 7 L9 7 L6 11 Z" fill="#8a0a0a"/><path d="M7 11 L21 11 L25 22 L3 22 Z" fill="#8a0a0a"/><circle cx="14" cy="16" r="3" fill="#e6e6e6"/></svg>
    <div class="call-text">Call Us Now!<br><b>03 5550 1827</b></div>
  </div>

  <div class="abs box reach">
    <div class="box-head">Service all of Australia</div>
    <p>95% of our clients come from client &amp; accountant referrals. We have client all over Victoria Queensland, NSW &amp; Western Australia<br><span>so no matter where you are we can help</span></p>
    <div class="abs map" role="img" aria-label="Map of Australia with client locations marked"></div>
  </div>

  <div class="abs box quals">
    <div class="box-head">Qualifications, Membership &amp; Partnership</div>
    <ul>
      <li><svg><use href="#tick-red"/></svg>Register ATO BAS agent</li>
      <li><svg><use href="#tick-red"/></svg>certified lv financial service</li>
      <li><svg><use href="#tick-red"/></svg>certified lll financial services</li>
      <li><svg><use href="#tick-red"/></svg>Member of institute of chartered bookkeepers</li>
      <li><svg><use href="#tick-red"/></svg>Platinum member of Australian bookkeepers</li>
      <li><svg><use href="#tick-red"/></svg>Ledgerline professional partner</li>
      <li><svg><use href="#tick-red"/></svg>Tax Savvy Network.</li>
    </ul>
  </div>

  <div class="abs badges">
    <div class="badge" style="width:45px;height:76px;background:#1d3f7a"></div>
    <div class="badge" style="width:70px;height:76px;background:#c33"></div>
    <div class="badge" style="width:95px;height:76px;background:#f06a1f"></div>
    <div class="badge" style="width:40px;height:76px;background:#222"></div>
    <div class="badge" style="width:147px;height:34px;background:#555"></div>
  </div>

  <div class="abs footer-rule"></div>
  <div class="abs follow">Follow Us <span class="sq"></span><span class="sq alt"></span></div>
  <div class="abs copy">Copyright © 2012 Barwick &amp; Lund. All Rights Reserved</div>
</div>
</body>
</html>
```